Halvard Hubs Business card

Halvard Hubs is a custom bicycle wheel builder. my current website can be viewed at www.halvardhubs.us
design features i am looking for include:
Logo with font used on website(911 porsche) with a gear graphic two meshed gears maybe
black background bright green logo and name
info to include:
front
Lemuel Castaby : owner/builder
ph; 555-418-7290
email sales@halvardhubs.us
www.halvardhubs.us
back
Brands availble:
Halvard Hubs Carbon
Ormo's
Tarvello
Rivosta
Dale Ferrow
Quorrin
Toplin Industries
Zelbrix
Ketro
Gandermark

```html
<!DOCTYPE html>
<html lang="en">
<head>
<meta charset="utf-8">
<title>Halvard Hubs — Business Card</title>
<link rel="stylesheet" href="https://fonts.googleapis.com/css2?family=Bodoni+Moda:wght@400&display=swap">
<style>
  :root {
    --card-black: #000000;
    --signal-green: #19ff19;
    --mark-green: #22f522;
  }
  html, body {
    margin: 0;
    padding: 0;
    width: 1200px;
    height: 667px;
    overflow: hidden;
    background: var(--card-black);
  }
  .card {
    position: relative;
    width: 1200px;
    height: 667px;
    background: var(--card-black);
    color: var(--signal-green);
    font-family: "Bodoni Moda", "Didot", serif;
    font-weight: 400;
  }
  .brand-dot {
    position: absolute;
    left: 178px;
    top: 97px;
    width: 300px;
    height: 300px;
  }
  .line {
    position: absolute;
    left: 420px;
    width: 780px;
    text-align: center;
    white-space: nowrap;
    margin: 0;
    line-height: 1;
  }
  .owner   { top: 56px;  font-size: 43px; }
  .phone   { top: 120px; font-size: 43px; }
  .email   { top: 502px; font-size: 41px; }
  .website { top: 566px; font-size: 41px; }
  .brand-name {
    position: absolute;
    left: 470px;
    width: 630px;
    text-align: center;
    margin: 0;
    font-size: 64px;
    line-height: 1;
    letter-spacing: 0.14em;
    text-transform: uppercase;
    color: var(--mark-green);
  }
  .brand-name .word { display: block; position: absolute; left: 0; width: 100%; }
  .brand-name .first  { top: 240px; }
  .brand-name .second { top: 368px; }
</style>
</head>
<body>
  <main class="card">
    <svg class="brand-dot" viewBox="0 0 300 300" aria-hidden="true">
      <circle cx="150" cy="150" r="150" fill="var(--mark-green)"/>
    </svg>

    <p class="line owner">Lemuel Castaby: Owner/Builder</p>
    <p class="line phone">Phone: 555-418-7290</p>

    <h1 class="brand-name" style="top:0;height:0;">
      <span class="word first">Halvard</span>
      <span class="word second">Hubs</span>
    </h1>

    <p class="line email">email: sales@halvardhubs.us</p>
    <p class="line website">www.halvardhubs.us</p>
  </main>
</body>
</html>
```